Kelvoranet.com Webpage Design

Design Brief for kelvoranet.com (Copy of Brief also in attached Word file)

Name of Website- kelvoranet.com (existing logo and look & feel of website to be changed)

Logo - Finalised. The logo files are attached with the brief as “logo.jpeg”. The “Blue- Grey” version of the logo is for use on lighter backgrounds and the “Orange-White” version of the logo is for use on darker backgrounds. (A full Black version of the logo is also attached). Both versions may be used in different parts of the website. All attached files are in .png format.
Status - The website in functional and is undergoing user trials. However, we want to improve the look & feel of the website so at it seems
a. cotemporary,
b. Easy to Navigate
c. professional and
d. Vibrant.

Please visit ‘kelvoranet.com’ to check out the website and its functionalities – please use it only as a reference for the features & functions to be provided, however the designer should use a ‘Free Hand’ in designing the composition of various parts of the webpage without getting too influenced by the existing design

Objective of the Website ‘kelvoranet.com –
a. It is a portal focussed on listing of ‘Retail’ specific real-estate properties by developers, owners and realty brokers. The properties shall listed under the following four categories-
i. Retail Malls
ii. Shopping Complexes
iii. High-street shops
iv. Retail Warehouses
*refer kelvoranet.com for better clarity

b. The abovementioned properties shall be listed either for ‘Sale’ or ‘rent\lease’ or both

c. Users shall visit the site in case they wish to acquire a retail \ shop space either on ‘sale’ or ‘rent’. These Users would be able to specify the ‘Search Criteria’ through the tool-bars provided on the website – the ‘Search Criteria’ shall comprise of ‘Type of space category’, ‘City’, ‘Locality’, transaction type ie ‘Rent \ Sale’ and ‘Area Range’

d. The main revenue model for the website shall be listing fee ( or advertising charges ) payable by those listing their properties on the website.

Three Main Pages of Website (kelvoranet.com) that need to be designed -
a. Main Home Page (visit the web link - http://kelvoranet.com/ ) - The main home page has the “Search Toolbar” for specifying of Search Criteria by the User. It shall also have the following features & functions-
i. Main Advertising Banner
ii. Featured Projects
iii. New Launches
iv. Toolbar with buttons – ‘Advertise with Us’, ‘Listings Alert’, ‘Quorra Desk’, ‘Advertiser Login’

b. Property Listings Page (visit the web link - http://kelvoranet.com/gurgaon-in-india ) - The List of property options that match the Criteria specified by the ‘User’ get displayed on this page.

c. Property Detail Page - When the ‘User’ clicks on the “More….” Button on the ‘Property Listings Page’ (given in point b. above) the web page with the details of the property opens. (For Example – visit the web link - http://kelvoranet.com/dorvik-Shopping-Complex-dorvik-bellmoor-gurgaon-636 )

Note:- Please refer to attached ‘Shopping’ related images the designer may use them on the website to provide a look & feel of retail if required – either separately or rotate in a single window

Target Market(s)

Retailers & Investors looking for retail space, Real Estate Brokers, Developers

Industry/Entity Type

Advertising

Number of Pages Required

3 page

Requirements
Must have
• Refer to existing site kelvoranet.com -- all the existing functionalities are a must have.
Nice to have
• The Designer may use the retail related images on the website if required for making it more vibrant. Refer attached images Shopping(1-6).jpg

```html
<!DOCTYPE html>
<html lang="en">
<head>
<meta charset="utf-8">
<title>Kelvoranet.com – Retail Space Portal</title>
<link rel="stylesheet" href="https://fonts.googleapis.com/css2?family=Montserrat:wght@400;500;600&family=Open+Sans:wght@400;600;700&display=swap">
<style>
:root{
  --orange:#f3a52c;
  --orange-dark:#d98b14;
  --ink:#333333;
  --ink-soft:#555555;
  --muted:#8a8a8a;
  --line:#e2e2e2;
  --white:#ffffff;
  --band:#6a6a6a;
  --band-dark:#5a5a5a;
  --footer:#2a2a2a;
  --tag-dark:#3a3a3a;
  --price:#5b5b5b;
}
*{box-sizing:border-box;margin:0;padding:0}
html,body{width:1200px;height:2404px;overflow:hidden;background:var(--white)}
body{position:relative;font-family:"Open Sans",Arial,sans-serif;color:var(--ink);font-size:12px}
.abs{position:absolute}
.head-font{font-family:"Montserrat",Arial,sans-serif}

/* top city strip */
.city-strip{top:0;left:0;width:1200px;height:19px;background:var(--orange);color:var(--white);font-size:10.5px;text-align:center;line-height:19px;font-weight:600;letter-spacing:.2px}

/* header */
.brand{top:26px;left:183px;display:flex;align-items:center;gap:8px}
.brand-dot{width:30px;height:30px;border-radius:50%;background:var(--ink)}
.brand-name{font-family:"Montserrat",sans-serif;font-weight:600;font-size:25px;color:var(--ink);line-height:1}
.brand-tag{top:62px;left:221px;font-size:7px;font-weight:700;letter-spacing:.5px;color:var(--ink)}
.contact-block{font-size:11px;color:var(--ink)}
.contact-block .label{color:var(--muted);display:flex;align-items:center;gap:5px}
.contact-block .label svg{width:9px;height:9px}
.phone-top{top:25px;left:708px}
.mail-top{top:25px;left:860px}

.nav-line{top:78px;left:172px;width:856px;height:1px;background:var(--line)}
.main-nav{top:86px;left:494px;display:flex;gap:30px;font-size:13px;color:var(--ink)}
.login-btn{top:78px;left:860px;width:150px;height:36px;background:var(--orange);border:1px solid var(--orange-dark);color:var(--ink);font-size:12.5px;display:flex;align-items:center;justify-content:center;gap:6px;font-weight:600}

/* hero */
.hero{top:115px;left:0;width:1200px;height:336px;background:linear-gradient(100deg,#c9a46a 0%,#e5cfa6 22%,#f2ece2 40%,#d88b3a 58%,#b45a2b 74%,#e8e2d8 88%,#a7906c 100%)}
.search-panel{top:374px;left:207px;width:788px;height:77px;background:var(--white);border-radius:6px 6px 0 0;padding:16px 10px 0 10px;display:flex;gap:15px}
.field label{display:block;font-size:10px;font-weight:700;color:var(--ink);margin-bottom:4px}
.field .box{width:111px;height:34px;border:1px solid #cfcfcf;font-size:11px;color:var(--ink-soft);display:flex;align-items:center;justify-content:space-between;padding:0 8px}
.field .box.wide{width:135px}
.caret{width:0;height:0;border-left:3px solid transparent;border-right:3px solid transparent;border-top:4px solid var(--ink)}
.search-btn{margin-top:14px;width:112px;height:34px;background:var(--orange);color:var(--white);font-weight:700;font-size:12px;display:flex;align-items:center;justify-content:center;gap:5px}

/* categories */
.category{width:220px;text-align:center}
.category .thumb{width:124px;height:124px;border-radius:50%;margin:0 auto;border:3px solid #eeeeee;box-shadow:0 0 0 1px #dddddd}
.category h3{font-family:"Montserrat",sans-serif;font-weight:500;font-size:19px;margin-top:36px;color:var(--ink)}
.category p{font-size:11px;color:var(--ink-soft);margin-top:6px}

/* section tags */
.section-tag{height:37px;display:flex;align-items:stretch;background:var(--orange);color:var(--white);font-family:"Montserrat",sans-serif;font-weight:600;font-size:12px}
.section-tag .icon{width:37px;background:var(--orange-dark);display:flex;align-items:center;justify-content:center}
.section-tag .text{padding:0 14px 0 12px;display:flex;align-items:center}
.slider-arrows{top:1389px;left:977px;display:flex;gap:6px}
.slider-arrows span{width:19px;height:19px;background:var(--orange);display:flex;align-items:center;justify-content:center}

/* property cards */
.card-row{left:172px;width:856px;display:flex;gap:23px}
.card{width:270px;height:263px;position:relative}
.card .photo{width:270px;height:166px;position:relative}
.deal{position:absolute;top:16px;left:14px;width:40px;height:40px;border-radius:50%;background:var(--white);font-size:11px;display:flex;align-items:center;justify-content:center;color:var(--ink)}
.pic-icon{position:absolute;right:8px;bottom:8px;width:14px;height:11px;border:1.5px solid var(--white);border-radius:1px}
.card .title-row{display:flex;justify-content:space-between;align-items:center;margin-top:10px;height:21px}
.card .title{border:1px solid var(--orange);font-size:12.5px;padding:1px 6px;color:var(--ink);white-space:nowrap}
.card .city{background:var(--tag-dark);color:var(--orange);font-size:12.5px;font-weight:600;padding:1px 6px 1px 5px;display:flex;align-items:center;gap:5px}
.card .meta-row{display:flex;justify-content:space-between;align-items:flex-start;margin-top:2px;height:34px}
.card .kind{font-size:11.5px;color:var(--ink);width:100px}
.card .price{background:var(--price);color:var(--white);font-size:10.5px;padding:3px 7px;margin-top:8px;white-space:nowrap}
.card .price small{font-size:9px;margin-right:6px}
.card .area{font-size:11px;color:var(--ink-soft);text-align:right;width:78px;line-height:1.3}
.card .stats{display:flex;margin-top:6px}
.card .stat{width:67.5px}
.card .stat b{display:block;font-weight:400;font-size:10.5px;color:var(--ink)}
.card .stat span{display:block;font-size:7.5px;color:var(--muted);margin-top:4px;letter-spacing:.2px}
.card .stat:last-child{text-align:right}

/* info band */
.info-band{top:1743px;left:0;width:1200px;height:416px;background:linear-gradient(180deg,var(--band) 0%,var(--band-dark) 100%)}
.band-title{font-family:"Montserrat",sans-serif;font-size:18px;color:var(--white);font-weight:500}
.alert-box{top:1786px;left:172px;width:270px;height:307px;background:var(--orange);padding:16px 7px 0 7px;color:var(--ink)}
.alert-box p{font-size:11px;line-height:1.45;margin-top:8px}
.input{height:23px;background:var(--white);border:1px solid #d0d0d0;font-size:11px;color:var(--muted);padding:0 6px;display:flex;align-items:center;justify-content:space-between}
.hint{font-size:11px;margin:6px 0 0 6px}
.btn-dark{height:21px;background:var(--tag-dark);color:var(--white);font-size:11px;display:flex;align-items:center;justify-content:center}
.desk-photo{top:1790px;left:468px;width:259px;height:117px;background:linear-gradient(120deg,#dfe3e8 0%,#f3f4f6 40%,#3d4048 70%,#9aa1aa 100%);border:2px solid var(--white)}
.band-text{font-size:11px;line-height:1.45;color:var(--white)}
.input.grey{background:#8a8a8a;border:none;color:#d5d5d5}
.thumb-grid{top:1932px;left:764px;width:255px;display:grid;grid-template-columns:repeat(3,80px);gap:8px 7px}
.thumb-grid div{height:70px}

/* footer */
.footer{top:2159px;left:0;width:1200px;height:216px;background:var(--footer)}
.foot-title{font-family:"Montserrat",sans-serif;font-size:15px;color:var(--white);font-weight:500}
.foot-text{font-size:11px;line-height:1.45;color:#d0d0d0}
.foot-list{list-style:none;font-size:10.5px;color:#d0d0d0;line-height:1.45}
.foot-list li{display:flex;align-items:center;gap:7px}
.foot-list li::before{content:"";width:4px;height:4px;border-radius:50%;background:var(--orange)}
.socials{display:flex;gap:3px}
.socials span{width:14px;height:14px;background:#555}
.foot-brand{top:2330px;left:890px;font-family:"Open Sans",sans-serif;font-size:17px;color:#6d6d6d}
.foot-brand-mark{top:2300px;left:935px;width:26px;height:26px;background:#4a4a4a}
.bottom-bar{top:2375px;left:0;width:1200px;height:29px;background:var(--orange);font-size:11px;color:var(--ink);line-height:29px;padding-left:183px}
</style>
</head>
<body>

<div class="abs city-strip">Bangalore | Chennai | Greater Noida | Gurgaon | Hyderabad | Jaipur | Khanna | Kolkatta | Mumbai | Noida | Pune | Surat |</div>

<header>
  <div class="abs brand"><span class="brand-dot"></span><span class="brand-name">kelvoranet</span></div>
  <div class="abs brand-tag">INDIA'S LEADING PORTAL FOR RETAIL SPACE</div>
  <div class="abs contact-block phone-top">
    <div class="label"><svg viewBox="0 0 10 10"><path d="M2 1h2l1 2-1.2 1a5 5 0 0 0 2.2 2.2L7 5l2 1v2a1 1 0 0 1-1 1A7 7 0 0 1 1 2a1 1 0 0 1 1-1z" fill="#f3a52c"/></svg>Contact Us</div>
    <div style="margin-top:3px">000-000-0000</div>
  </div>
  <div class="abs contact-block mail-top">
    <div class="label"><svg viewBox="0 0 10 10"><rect x="0.5" y="2" width="9" height="6" fill="none" stroke="#f3a52c"/><path d="M0.5 2l4.5 3.5L9.5 2" fill="none" stroke="#f3a52c"/></svg>Email Us</div>
    <div style="margin-top:3px">kelvoranet@lorem.com</div>
    <div style="margin-top:2px">List Your Property Here</div>
  </div>
  <div class="abs nav-line"></div>
  <nav class="abs main-nav"><span>Advertise with us</span><span>Quorra Desk</span><span>Listing Alert</span></nav>
  <div class="abs login-btn">
    <svg width="10" height="11" viewBox="0 0 10 11"><path d="M5 1a3 3 0 0 1 3 3v3l1 2H1l1-2V4a3 3 0 0 1 3-3z" fill="#fff"/></svg>
    Advertiser Login <span class="caret" style="border-top-color:#fff;margin-left:6px"></span>
  </div>
</header>

<section class="abs hero" role="img" aria-label="Banner photo of a smiling shopper holding shopping bags inside a bright mall atrium"></section>

<form class="abs search-panel">
  <div class="field"><label>Select Properties</label><div class="box">Select... <span class="caret"></span></div></div>
  <div class="field"><label>Sale or Rent or Both</label><div class="box">Any <span class="caret"></span></div></div>
  <div class="field"><label>City</label><div class="box">Select <span class="caret"></span></div></div>
  <div class="field"><label>Location</label><div class="box">Select <span class="caret"></span></div></div>
  <div class="field"><label>Enter Keywords</label><div class="box wide"></div></div>
  <div class="search-btn"><svg width="11" height="11" viewBox="0 0 11 11"><circle cx="4.5" cy="4.5" r="3.3" fill="none" stroke="#fff" stroke-width="1.6"/><path d="M7 7l3 3" stroke="#fff" stroke-width="1.8"/></svg>Search</div>
</form>

<section class="categories">
  <div class="abs category" style="top:490px;left:162px">
    <div class="thumb" role="img" aria-label="Photo of a retail mall building" style="background:linear-gradient(180deg,#8fb2d6 0%,#c9d6e4 45%,#6b6f78 75%,#9a8f84 100%)"></div>
    <h3>Retail Malls</h3><p>Centrally Air-Conditioned</p>
  </div>
  <div class="abs category" style="top:490px;left:382px">
    <div class="thumb" role="img" aria-label="Photo of a shopping complex building" style="background:linear-gradient(180deg,#5b84b8 0%,#a9bcd2 45%,#d9c7a4 75%,#8d8a82 100%)"></div>
    <h3>Shopping Complex</h3><p>Non Air-Conditioned Building</p>
  </div>
  <div class="abs category" style="top:490px;left:602px">
    <div class="thumb" role="img" aria-label="Photo of a retail warehouse interior" style="background:linear-gradient(180deg,#dfe4dc 0%,#7fb55c 45%,#a89c86 75%,#d4cfc4 100%)"></div>
    <h3>Retail Warehouses</h3><p>Back-end Retail Storage</p>
  </div>
  <div class="abs category" style="top:490px;left:820px">
    <div class="thumb" role="img" aria-label="Photo of road facing high street shops" style="background:linear-gradient(180deg,#c7d2dc 0%,#8e98a6 40%,#b9825a 70%,#5d5a56 100%)"></div>
    <h3>High Street Shops</h3><p>Road Facing Retail</p>
  </div>
</section>

<div class="abs section-tag" style="top:742px;left:172px">
  <span class="icon"><svg width="14" height="14" viewBox="0 0 14 14"><path d="M2 12C2 6 6 2 12 2c0 6-4 10-10 10z" fill="#fff"/></svg></span><span class="text">Recent Projects</span>
</div>

<!-- recent row 1 -->
<div class="abs card-row" style="top:801px">
  <article class="card">
    <div class="photo" role="img" aria-label="Night photo of a lit mall entrance" style="background:linear-gradient(160deg,#1f2b4a 0%,#3b4a78 40%,#c98a3c 70%,#2a2a3a 100%)"><span class="deal">Sale</span><span class="pic-icon"></span></div>
    <div class="title-row"><span class="title">Orvel Mall</span><span class="city"><svg width="8" height="10" viewBox="0 0 8 10"><path d="M4 0a4 4 0 0 1 4 4c0 3-4 6-4 6S0 7 0 4a4 4 0 0 1 4-4z" fill="#f3a52c"/><circle cx="4" cy="4" r="1.4" fill="#3a3a3a"/></svg>Bangalore</span></div>
    <div class="meta-row"><span class="kind">Retail Malls</span><span class="price"><small>Rs</small>5000000</span><span class="area">Malleshwaram</span></div>
    <div class="stats"><div class="stat"><b>1000 Sq ft</b><span>SHOP AREA</span></div><div class="stat"><b>4</b><span>TOTAL FLOOR</span></div><div class="stat"><b>YES</b><span>PARKING</span></div><div class="stat"><b>YES</b><span>CENTRAL AC</span></div></div>
  </article>
  <article class="card">
    <div class="photo" role="img" aria-label="Photo of a modern glass commercial building" style="background:linear-gradient(170deg,#6f8fbf 0%,#a8bddb 40%,#3e5a82 70%,#8d9198 100%)"><span class="deal">Rent</span><span class="pic-icon"></span></div>
    <div class="title-row"><span class="title">Tarvin Trinity</span><span class="city"><svg width="8" height="10" viewBox="0 0 8 10"><path d="M4 0a4 4 0 0 1 4 4c0 3-4 6-4 6S0 7 0 4a4 4 0 0 1 4-4z" fill="#f3a52c"/><circle cx="4" cy="4" r="1.4" fill="#3a3a3a"/></svg>Gurgaon</span></div>
    <div class="meta-row"><span class="kind">Shopping Complex</span><span class="price"><small>Rs</small>300000</span><span class="area">Dwarka Expressway</span></div>
    <div class="stats"><div class="stat"><b>1000 Sq ft</b><span>SHOP AREA</span></div><div class="stat"><b>5</b><span>TOTAL FLOOR</span></div><div class="stat"><b>YES</b><span>PARKING</span></div><div class="stat"><b>YES</b><span>CENTRAL AC</span></div></div>
  </article>
  <article class="card">
    <div class="photo" role="img" aria-label="Photo of a mall facade under a blue sky" style="background:linear-gradient(180deg,#7fa6d8 0%,#c3d3e6 40%,#6a6f80 70%,#a59e92 100%)"><span class="deal">Sale</span><span class="pic-icon"></span></div>
    <div class="title-row"><span class="title">Larkway Mall</span><span class="city"><svg width="8" height="10" viewBox="0 0 8 10"><path d="M4 0a4 4 0 0 1 4 4c0 3-4 6-4 6S0 7 0 4a4 4 0 0 1 4-4z" fill="#f3a52c"/><circle cx="4" cy="4" r="1.4" fill="#3a3a3a"/></svg>Mysore</span></div>
    <div class="meta-row"><span class="kind">Retail Malls</span><span class="price"><small>Rs</small>3500000</span><span class="area">Hunsur Main Road</span></div>
    <div class="stats"><div class="stat"><b>1300 Sq ft</b><span>SHOP AREA</span></div><div class="stat"><b>3</b><span>TOTAL FLOOR</span></div><div class="stat"><b>YES</b><span>PARKING</span></div><div class="stat"><b>YES</b><span>CENTRAL AC</span></div></div>
  </article>
</div>

<!-- recent row 2 -->
<div class="abs card-row" style="top:1088px">
  <article class="card">
    <div class="photo" role="img" aria-label="Photo of a mall plaza with a fountain" style="background:linear-gradient(180deg,#b8c2cc 0%,#d9dde2 40%,#7a6a5e 70%,#a89e90 100%)"><span class="deal">Rent</span><span class="pic-icon"></span></div>
    <div class="title-row"><span class="title">The Grand Vale Place</span><span class="city"><svg width="8" height="10" viewBox="0 0 8 10"><path d="M4 0a4 4 0 0 1 4 4c0 3-4 6-4 6S0 7 0 4a4 4 0 0 1 4-4z" fill="#f3a52c"/><circle cx="4" cy="4" r="1.4" fill="#3a3a3a"/></svg>Bhopal</span></div>
    <div class="meta-row"><span class="kind">Retail Malls</span><span class="price"><small>Rs</small>75000</span><span class="area">Kolar Road</span></div>
    <div class="stats"><div class="stat"><b>1600 Sq ft</b><span>SHOP AREA</span></div><div class="stat"><b>5</b><span>TOTAL FLOOR</span></div><div class="stat"><b>YES</b><span>PARKING</span></div><div class="stat"><b>YES</b><span>CENTRAL AC</span></div></div>
  </article>
  <article class="card">
    <div class="photo" role="img" aria-label="Rendering of a shopping complex with palm trees and parking" style="background:linear-gradient(180deg,#a9c4e0 0%,#d8dfe6 40%,#8a8c86 65%,#5f6a54 100%)"><span class="deal">Sale</span><span class="pic-icon"></span></div>
    <div class="title-row"><span class="title">SCO In Sector 127 On</span><span class="city"><svg width="8" height="10" viewBox="0 0 8 10"><path d="M4 0a4 4 0 0 1 4 4c0 3-4 6-4 6S0 7 0 4a4 4 0 0 1 4-4z" fill="#f3a52c"/><circle cx="4" cy="4" r="1.4" fill="#3a3a3a"/></svg>Mohali</span></div>
    <div class="meta-row"><span class="kind">Shopping Complex</span><span class="price"><small>Rs</small>4400000</span><span class="area">Sihon Majra</span></div>
    <div class="stats"><div class="stat"><b>1100 Sq ft</b><span>SHOP AREA</span></div><div class="stat"><b>3</b><span>TOTAL FLOOR</span></div><div class="stat"><b>YES</b><span>PARKING</span></div><div class="stat"><b>YES</b><span>CENTRAL AC</span></div></div>
  </article>
  <article class="card">
    <div class="photo" role="img" aria-label="Photo of a warmly lit mall interior" style="background:linear-gradient(180deg,#5a3a22 0%,#b3773a 40%,#e2b27a 65%,#7a5434 100%)"><span class="deal">Sale</span><span class="pic-icon"></span></div>
    <div class="title-row"><span class="title">Crest One</span><span class="city"><svg width="8" height="10" viewBox="0 0 8 10"><path d="M4 0a4 4 0 0 1 4 4c0 3-4 6-4 6S0 7 0 4a4 4 0 0 1 4-4z" fill="#f3a52c"/><circle cx="4" cy="4" r="1.4" fill="#3a3a3a"/></svg>Noida</span></div>
    <div class="meta-row"><span class="kind">Retail Malls</span><span class="price"><small>Rs</small>6500000</span><span class="area">Sector-18</span></div>
    <div class="stats"><div class="stat"><b>1250 Sq ft</b><span>SHOP AREA</span></div><div class="stat"><b>5</b><span>TOTAL FLOOR</span></div><div class="stat"><b>YES</b><span>PARKING</span></div><div class="stat"><b>YES</b><span>CENTRAL AC</span></div></div>
  </article>
</div>

<div class="abs section-tag" style="top:1378px;left:172px">
  <span class="icon"><svg width="14" height="14" viewBox="0 0 14 14"><path d="M2 12C2 6 6 2 12 2c0 6-4 10-10 10z" fill="#fff"/></svg></span><span class="text">Featured Projects</span>
</div>
<div class="abs slider-arrows">
  <span><svg width="7" height="9" viewBox="0 0 7 9"><path d="M6 0.5L1.5 4.5 6 8.5" fill="none" stroke="#fff" stroke-width="1.6"/></svg></span>
  <span><svg width="7" height="9" viewBox="0 0 7 9"><path d="M1 0.5L5.5 4.5 1 8.5" fill="none" stroke="#fff" stroke-width="1.6"/></svg></span>
</div>

<!-- featured row -->
<div class="abs card-row" style="top:1439px">
  <article class="card">
    <div class="photo" role="img" aria-label="Photo of a mall exterior with billboards" style="background:linear-gradient(180deg,#9db4cc 0%,#c9d2da 35%,#5e6670 65%,#8e8a84 100%)"><span class="deal">Sale</span><span class="pic-icon"></span></div>
    <div class="title-row"><span class="title">Halcyon Mall</span><span class="city"><svg width="8" height="10" viewBox="0 0 8 10"><path d="M4 0a4 4 0 0 1 4 4c0 3-4 6-4 6S0 7 0 4a4 4 0 0 1 4-4z" fill="#f3a52c"/><circle cx="4" cy="4" r="1.4" fill="#3a3a3a"/></svg>New Delhi</span></div>
    <div class="meta-row"><span class="kind">Retail Malls</span><span class="price"><small>Rs</small>4750000</span><span class="area">Tagore Garden</span></div>
    <div class="stats"><div class="stat"><b>1550 Sq ft</b><span>SHOP AREA</span></div><div class="stat"><b>5</b><span>TOTAL FLOOR</span></div><div class="stat"><b>YES</b><span>PARKING</span></div><div class="stat"><b>YES</b><span>CENTRAL AC</span></div></div>
  </article>
  <article class="card">
    <div class="photo" role="img" aria-label="Dusk rendering of a lit high street building" style="background:linear-gradient(180deg,#1d2f5a 0%,#3c5896 40%,#d9a25a 70%,#3a3036 100%)"><span class="deal">Rent</span><span class="pic-icon"></span></div>
    <div class="title-row"><span class="title">Vesta 81 High Street</span><span class="city"><svg width="8" height="10" viewBox="0 0 8 10"><path d="M4 0a4 4 0 0 1 4 4c0 3-4 6-4 6S0 7 0 4a4 4 0 0 1 4-4z" fill="#f3a52c"/><circle cx="4" cy="4" r="1.4" fill="#3a3a3a"/></svg>Faridabad</span></div>
    <div class="meta-row"><span class="kind">Shopping Complex</span><span class="price"><small>Rs</small>45000</span><span class="area">Sector-81</span></div>
    <div class="stats"><div class="stat"><b>1300 Sq ft</b><span>SHOP AREA</span></div><div class="stat"><b>8</b><span>TOTAL FLOOR</span></div><div class="stat"><b>YES</b><span>PARKING</span></div><div class="stat"><b>YES</b><span>CENTRAL AC</span></div></div>
  </article>
  <article class="card">
    <div class="photo" role="img" aria-label="Photo of a curved glass shopping complex" style="background:linear-gradient(180deg,#c4d6ea 0%,#6f9ac8 40%,#2f5a92 65%,#b3b6ba 100%)"><span class="deal">Rent</span><span class="pic-icon"></span></div>
    <div class="title-row"><span class="title">Norvan Galleria 91</span><span class="city"><svg width="8" height="10" viewBox="0 0 8 10"><path d="M4 0a4 4 0 0 1 4 4c0 3-4 6-4 6S0 7 0 4a4 4 0 0 1 4-4z" fill="#f3a52c"/><circle cx="4" cy="4" r="1.4" fill="#3a3a3a"/></svg>Gurgaon</span></div>
    <div class="meta-row"><span class="kind">Shopping Complex</span><span class="price"><small>Rs</small>25000</span><span class="area">Golf Course Road</span></div>
    <div class="stats"><div class="stat"><b>850 Sq ft</b><span>SHOP AREA</span></div><div class="stat"><b>4</b><span>TOTAL FLOOR</span></div><div class="stat"><b>YES</b><span>PARKING</span></div><div class="stat"><b>YES</b><span>CENTRAL AC</span></div></div>
  </article>
</div>

<!-- info band -->
<section class="abs info-band"></section>
<h2 class="abs band-title" style="top:1754px;left:174px">Listing Alert</h2>
<h2 class="abs band-title" style="top:1754px;left:470px">Quorra Desk</h2>
<h2 class="abs band-title" style="top:1754px;left:764px">Editor's Choice</h2>

<div class="abs alert-box">
  <svg width="42" height="30" viewBox="0 0 42 30" style="margin-left:3px"><rect x="1.5" y="1.5" width="39" height="27" fill="none" stroke="#fff" stroke-width="2.5"/><path d="M1.5 1.5L21 17 40.5 1.5" fill="none" stroke="#fff" stroke-width="2.5"/></svg>
  <p>Subscribe for Fortnightly Email update on New Listings @ Kelvoranet</p>
  <div class="input" style="margin-top:17px">Email address</div>
  <div class="input" style="margin-top:27px">Select Options <span class="caret"></span></div>
  <div class="hint">(select retail format of interest)</div>
  <div class="input" style="margin-top:17px">Location <span class="caret"></span></div>
  <div class="hint" style="margin-top:10px">(Select cities of interest)</div>
</div>
<div class="abs btn-dark" style="top:2103px;left:370px;width:72px">Subscribe</div>

<div class="abs desk-photo" role="img" aria-label="Photo of business people meeting in an office"></div>
<p class="abs band-text" style="top:1914px;left:468px;width:262px">Post your Retail Space requirement with us and our experts shall get back with suitable options and even help you in your transaction. This is a Free Service!</p>
<div class="abs input grey" style="top:1988px;left:468px;width:259px;height:20px">Your email address...</div>
<div class="abs input grey" style="top:2016px;left:468px;width:259px;height:20px">Mobile...</div>
<div class="abs input grey" style="top:2044px;left:468px;width:259px;height:48px;align-items:flex-start;padding-top:4px">Message...</div>
<div class="abs btn-dark" style="top:2103px;left:675px;width:52px">Send</div>

<p class="abs band-text" style="top:1786px;left:764px;width:258px">A "Select" Listing of Retail Properties Handpicked by our Editors based on their own positive evaluation on parameters &amp; attributes such as Design Concept,Location, Developer, Success Potential.</p>
<div class="abs thumb-grid">
  <div role="img" aria-label="Thumbnail photo of a mall building" style="background:linear-gradient(180deg,#7da3d4,#c2cedb 50%,#6d6f76)"></div>
  <div role="img" aria-label="Thumbnail photo of a shopping complex at dusk" style="background:linear-gradient(180deg,#2a3b66,#6f7fa6 50%,#c48a44)"></div>
  <div role="img" aria-label="Thumbnail photo of a retail building" style="background:linear-gradient(180deg,#9fb7d6,#dfe3e8 50%,#8a7f76)"></div>
  <div role="img" aria-label="Thumbnail photo of a glass retail tower" style="background:linear-gradient(180deg,#6b93c9,#b4c8e0 50%,#55627a)"></div>
  <div role="img" aria-label="Thumbnail photo of a shopping plaza" style="background:linear-gradient(180deg,#b9c7d6,#e3e6ea 50%,#9b8a78)"></div>
  <div role="img" aria-label="Thumbnail photo of a modern mall facade" style="background:linear-gradient(180deg,#4f7ab3,#a7bfdc 50%,#3e4e68)"></div>
</div>
<div class="abs btn-dark" style="top:2103px;left:948px;width:71px">Read more</div>

<!-- footer -->
<footer class="abs footer"></footer>
<h3 class="abs foot-title" style="top:2186px;left:178px">About Us</h3>
<p class="abs foot-text" style="top:2220px;left:172px;width:280px">Kelvoranet.com is a Specialised Web based platform for Retail Space, featuring properties across India under various formats such as Retail Malls, Shopping Complexes, High-street Shops. Also featured are 'Retail Warehouses' which provide the logistic back-end for the retail business. Kelvoranet.com is useful to various category of users as follows- a. Devel</p>

<h3 class="abs foot-title" style="top:2186px;left:476px">Contact Us</h3>
<div class="abs foot-text" style="top:2218px;left:476px;display:flex;gap:12px">
  <svg width="8" height="10" viewBox="0 0 8 10" style="margin-top:3px"><path d="M4 0a4 4 0 0 1 4 4c0 3-4 6-4 6S0 7 0 4a4 4 0 0 1 4-4z" fill="#f3a52c"/><circle cx="4" cy="4" r="1.4" fill="#2a2a2a"/></svg>
  <div>Halden Retail<br>Unit 218, 2nd Floor,<br>Sector-x, Gurgaon - 122002</div>
</div>
<div class="abs foot-text" style="top:2276px;left:476px;display:flex;gap:10px;align-items:center">
  <svg width="10" height="10" viewBox="0 0 10 10"><path d="M2 1h2l1 2-1.2 1a5 5 0 0 0 2.2 2.2L7 5l2 1v2a1 1 0 0 1-1 1A7 7 0 0 1 1 2a1 1 0 0 1 1-1z" fill="#f3a52c"/></svg>000-000-0000
</div>
<div class="abs foot-text" style="top:2304px;left:476px;display:flex;gap:10px;align-items:center">
  <svg width="10" height="10" viewBox="0 0 10 10"><rect x="1" y="3" width="8" height="5" fill="none" stroke="#f3a52c" stroke-width="1.4"/><rect x="3" y="1" width="4" height="2.5" fill="#f3a52c"/></svg>000-000-0000
</div>
<div class="abs socials" style="top:2334px;left:486px"><span></span><span></span><span></span><span></span></div>

<h3 class="abs foot-title" style="top:2186px;left:688px">About Halden Retail</h3>
<ul class="abs foot-list" style="top:2218px;left:690px">
  <li>About Us</li><li>Retail Malls</li><li>Shopping Complex</li><li>High Street Shops</li><li>Retail Warehouses</li>
</ul>
<ul class="abs foot-list" style="top:2218px;left:838px">
  <li>Privacy Policy</li><li>Terms of Use</li><li>Site Map</li><li>Contact Us</li>
</ul>
<div class="abs foot-brand-mark"></div>
<div class="abs foot-brand">Halden Retail</div>

<div class="abs bottom-bar">Copyright © 2013 India Halden Retail.com. All rights reserved.</div>

</body>
</html>
```